Business cards Dorn Kelterhof GmbH & Co.KG

We need a uniform business card design template for our employees.
A template should be created to have the same design for all business cards.

Contact Information for Business Card

Firma und Firmierung, Name, Funktion in Unternehmen, Anschrift, Tel. Handynummer, Emailadresse, Internetseite

Colors

Designer to choose colors to be used in the design.

Requirements
Must have
• Our company logo must be on it

```html
<!DOCTYPE html>
<html lang="de">
<head>
<meta charset="utf-8">
<title>Dorn Kelterhof – Visitenkarten</title>
<link rel="stylesheet" href="https://fonts.googleapis.com/css2?family=PT+Sans&family=Tinos&display=swap">
<style>
  :root {
    --backdrop: #3b3431;
    --card: #0d0b0c;
    --card-edge: #1b1719;
    --lavender: #c9a2d8;
    --rose: #e2587c;
    --divider: #2a2427;
  }
  * { margin: 0; padding: 0; box-sizing: border-box; }
  html, body {
    width: 1200px; height: 844px; overflow: hidden;
    background: var(--backdrop);
  }
  .sheet {
    position: relative; width: 1200px; height: 844px;
    display: flex; align-items: center; justify-content: center; gap: 60px;
  }
  .card {
    position: relative; width: 520px; height: 297px;
    background: var(--card);
    border: 1px solid var(--card-edge);
    box-shadow: 0 10px 30px rgba(0,0,0,.45);
  }
  .wordmark {
    font-family: "PT Sans", sans-serif;
    color: var(--lavender);
    letter-spacing: .04em;
    text-transform: uppercase;
    white-space: nowrap;
  }
  /* contact side */
  .card--contact .brand {
    position: absolute; left: 0; top: 0; width: 260px; height: 100%;
    display: flex; align-items: center; justify-content: center;
    border-right: 1px solid var(--divider);
  }
  .card--contact .wordmark { font-size: 24px; }
  .details {
    position: absolute; left: 288px; top: 62px; width: 220px;
    font-family: "PT Sans", sans-serif; color: var(--lavender);
    font-size: 13.5px; line-height: 1.3;
  }
  .details .name {
    font-family: "Tinos", serif; color: var(--rose);
    font-size: 19px; letter-spacing: .03em; font-weight: 400;
  }
  .details .role { margin-bottom: 16px; }
  .details .address { margin-bottom: 14px; }
  .contact-list { list-style: none; }
  .contact-list li { display: flex; align-items: center; gap: 8px; }
  .contact-list svg { width: 10px; height: 10px; flex: none; fill: var(--rose); }
  /* logo side */
  .card--logo { display: flex; align-items: center; justify-content: center; }
  .card--logo .wordmark { font-size: 38px; }
</style>
</head>
<body>
<main class="sheet">
  <section class="card card--contact">
    <div class="brand"><span class="wordmark">Dorn Kelterhof</span></div>
    <div class="details">
      <h1 class="name">LUKAS BERGER</h1>
      <p class="role">Managing Director</p>
      <p class="address">12345, Address Goes Here<br>Country Name, 123456.</p>
      <ul class="contact-list">
        <li><svg viewBox="0 0 10 10" aria-hidden="true"><path d="M1 3c0-1 1-2 2-2l1 2-1 1c.5 1 1.5 2 3 3l1-1 2 1c0 1-1 2-2 2C4 9 1 6 1 3z"/></svg>044-987 654 321</li>
        <li><svg viewBox="0 0 10 10" aria-hidden="true"><path d="M0 2h10v6H0z M0 2l5 3.5L10 2" stroke="#0d0b0c" stroke-width=".8"/></svg>info@kelterhof-mail.de</li>
        <li><svg viewBox="0 0 10 10" aria-hidden="true"><path d="M2 8l6-6M1.5 6.5l-1 1a1.4 1.4 0 0 0 2 2l1-1M8.5 3.5l1-1a1.4 1.4 0 0 0-2-2l-1 1" stroke="#e2587c" stroke-width="1.2" fill="none"/></svg>www.kelterhof-beispiel.de</li>
      </ul>
    </div>
  </section>
  <section class="card card--logo">
    <span class="wordmark">Dorn Kelterhof</span>
  </section>
</main>
</body>
</html>
```